International E-Shop Needs a Web Design

I need a web design for a new e-shop based in UK, called Voph. This will be an international collective buying website. I would like to see designs that use the colors orange and green (similar to logo colors). However, any other ideas and your vision are also welcome. The brand image is associated with words fun, social, cool and simple. The final design should look very modern and unique. Please also take into consideration user experience.

I have attached logo design. Please ignore the black background, it would be better if you extract only the name Voph on the logo design. I have also attached one example of website design which I like (especially it's modern style, bramblenest.com) and two screenshots showing icons that visualize each category (which I want to appear in my main menu bar).

*UPDATE: There is something wrong with the system and I can't upload other 3 files (web design example and 2 examples of icons). If you could give me your e-mail, then I could send all these files to you. Anyway, what I think is a modern design can be viewed on bramblenest.com

If you have any further questions, do not hesitate to ask. Thank you in advance and I look forward to your outstanding designs!

Target Market(s)

My target customers are people both male and female in the age group of 18-45 years old, who are shopping online and are present on social media.

Industry/Entity Type

Shop

Requirements
Must have
• - "What is Voph?" Button
- Log In / Register Buttons
- Currency Sliding Menu
- Shopping Cart
- "How to Buy?" and "How to Sell?" Buttons
- Follow us on Linkpond, Quillo, Zembra+
- Like Button with a number of people who like this.
- Check-In Button
- RSS Feed
- Main Menu with categories and buttons, such as Home, Electronics, Entertainment & Leisure, Fashion, Health & Beauty, Home & Garden, Jewellery & Watches, Sports & Outdoors. I would like to see also small pictures (icons) that would symbolize each category.
- Search Bar
- Carousel Slideshow with 5 different slides. The first slide on carousel slideshow should be welcoming! Something like: "Welcome to Voph! Why to shop at Voph?" - This slide should be designed in a similar way as the website.
- Four Main Categories: Latest Bargains, Your Recently Viewed Bargains, Ending Soon Bargains, Popular Bargains
- Under Each Category should be at least 3 products
- Users will be allowed to upload their own pictures, which means that picture quality and design will be different. Some kind of frames around pictures or something else (under one style) to make pictures look similar would be very helpful.
- Each Product should show the following information: Main Photo, Name, Description (Short), Total Discount (for example 35%), Current Discount (for example 5%), Starting Price, Current Price, Time Left on Bargain: 7:1:45:30
- The final design should be delivered in Photoshop format file (PSD file).
Should not have
• The choice of colors shouldn't be aggressive. Instead it should be calm and gentle. So that the user would feel himself comfortable while browsing the website.

```html
<!DOCTYPE html>
<html lang="en">
<head>
<meta charset="utf-8">
<title>Voph – Change the way you shop</title>
<link rel="stylesheet" href="https://fonts.googleapis.com/css2?family=Kalam:wght@400;700&family=Open+Sans:ital,wght@0,400;0,600;0,700;0,800;1,800&display=swap">
<style>
:root{
  --orange:#f26a1b;
  --orange-dark:#c94a0a;
  --green:#7cc242;
  --green-dark:#4e8f1f;
  --bar:#2b2d30;
  --panel-light:#8a8d91;
  --panel-dark:#5b5e62;
  --page-light:#6f7276;
  --page-dark:#3b3d40;
  --section-head:#2f3135;
  --text-light:#f2f2f2;
  --sale-red:#d8261c;
  --frame:#e8a01e;
}
*{box-sizing:border-box;margin:0;padding:0}
html,body{width:1200px;height:2847px;overflow:hidden}
body{
  font-family:"Open Sans",Arial,sans-serif;color:var(--text-light);
  background:linear-gradient(90deg,var(--page-light) 0 597px,var(--page-dark) 597px 100%);
  position:relative;
}
.hand{font-family:"Kalam",cursive}
/* top bar */
.topbar{position:absolute;left:0;top:0;width:1200px;height:76px;background:var(--bar);border-bottom:4px solid var(--green);display:flex;align-items:center;padding:0 40px;white-space:nowrap}
.topbar a{color:#ddd;text-decoration:none;font-family:"Kalam",cursive;font-size:27px;padding:0 26px;border-right:2px solid var(--green)}
.topbar a:first-child{padding-left:10px}
.topbar .spacer{flex:1}
.topbar .account a{border:none;border-left:2px solid var(--green)}
.topbar .account a:first-child{border-left:none}
.tab-flag{position:absolute;top:0;width:22px;height:86px;background:var(--green)}
/* header */
.header{position:absolute;left:0;top:80px;width:1200px;height:120px}
.logo{position:absolute;left:40px;top:14px;font-size:84px;font-weight:800;color:var(--orange);line-height:1}
.search{position:absolute;left:315px;top:50px;width:605px;height:54px;display:flex;border-radius:8px;overflow:hidden;box-shadow:0 2px 4px #0008;white-space:nowrap}
.search .cat{width:192px;background:#fff;color:#222;font-weight:700;font-size:18px;display:flex;align-items:center;justify-content:space-between;padding:0 18px;border-right:2px solid #999}
.search .field{flex:1;background:#fff;color:#999;font-size:19px;display:flex;align-items:center;padding-left:14px}
.search .go{width:168px;background:linear-gradient(#ffd23a,#e8a200);color:#3a2a00;font-weight:700;font-size:20px;display:flex;align-items:center;justify-content:center;gap:10px}
.checkout{position:absolute;left:948px;top:48px;width:220px;height:58px;background:#1e1f21;border-radius:6px;display:flex;align-items:center;padding:0 14px;gap:12px;font-weight:800;font-size:21px;white-space:nowrap}
.checkout .arr{margin-left:auto;width:36px;height:36px;background:#333;border-radius:4px;display:flex;align-items:center;justify-content:center;color:var(--green)}
/* nav */
.nav{position:absolute;left:0;top:200px;width:1200px;height:95px;background:linear-gradient(#55585c,#3e4044)}
.nav .rail{position:absolute;left:0;right:0;top:16px;height:6px;background:var(--green)}
.nav ul{list-style:none;display:flex;height:95px;position:relative}
.nav li{flex:none;text-align:center;font-size:17px;font-weight:600;color:#fff;text-transform:uppercase;line-height:1.1;display:flex;flex-direction:column;align-items:center;justify-content:flex-end;padding-bottom:14px;border-right:2px solid #2a2b2e;white-space:nowrap}
.nav li svg{position:absolute;top:0}
.nav .knob{position:absolute;left:1010px;top:2px;width:26px;height:80px;background:#e9e9e9;border-radius:12px;border:3px solid var(--green)}
/* hero */
.carousel{position:absolute;left:25px;top:320px;width:752px;height:432px;border:3px solid var(--frame);background:linear-gradient(135deg,#d9d9d9,#7a7a7a 55%,#3a3a3a)}
.carousel .label{position:absolute;background:#1c1c1ccc;color:#fff;font-size:16px;padding:8px 12px}
.carousel .arrow{position:absolute;top:190px;width:34px;height:50px;background:#fff;color:#222;display:flex;align-items:center;justify-content:center;font-size:20px}
.carousel .welcome{position:absolute;right:22px;top:300px;text-align:right;font-weight:800;font-style:italic;font-size:27px;line-height:1.2;text-transform:uppercase;text-shadow:0 2px 3px #000;white-space:nowrap}
.carousel .tour{position:absolute;right:22px;bottom:14px;font-size:21px;letter-spacing:1px;text-transform:uppercase;white-space:nowrap}
.quick{position:absolute;left:827px;top:340px;width:325px}
.quick .intro{font-size:25px;margin-left:35px;margin-bottom:18px}
.quick a{display:flex;align-items:center;justify-content:center;height:55px;margin-bottom:37px;border-radius:28px;background:linear-gradient(#ff8a2a,#e24f06);border:3px solid #3a1a08;box-shadow:0 3px 5px #000a;color:#fff;font-family:"Kalam",cursive;font-size:25px;text-decoration:none;white-space:nowrap}
/* newsletter */
.newsletter{position:absolute;left:0;top:773px;width:1200px;height:56px;background:#4a4d50;border-top:3px solid var(--green);display:flex;align-items:center;padding-left:12px;gap:12px;white-space:nowrap}
.newsletter .ask{font-size:21px;color:var(--green)}
.newsletter .email{width:400px;height:42px;background:#e6ecdc;color:#555;font-size:20px;display:flex;align-items:center;padding-left:14px}
.newsletter .btn{height:44px;background:#b8bcbf;color:#222;font-size:18px;display:flex;align-items:center;padding:0 22px;border-radius:3px}
.newsletter .rss{margin-left:auto;margin-right:10px;width:400px;justify-content:space-between}
.rss-ico{width:28px;height:28px;background:#333;border-radius:4px}
/* sections */
.bargains{position:absolute;left:0;width:1200px;height:400px}
.bargains .head{height:52px;background:var(--section-head);display:flex;align-items:center;padding:0 30px;font-family:"Kalam",cursive;font-size:25px;position:relative;white-space:nowrap}
.bargains.right .head{justify-content:flex-end}
.bargains .ribbon{position:absolute;top:-4px;width:22px;height:86px;clip-path:polygon(0 0,100% 0,100% 100%,50% 86%,0 100%)}
.bargains .body{height:348px;background:linear-gradient(90deg,var(--panel-light),#7c7f83 50%,var(--panel-dark));border-top:2px solid var(--orange);border-bottom:2px solid var(--orange);position:relative}
.product{position:absolute;top:20px;width:320px}
.product .photo{height:222px;border:4px solid var(--frame);box-shadow:0 4px 6px #0006}
.ph-room{background:linear-gradient(#4a3a28,#b08a4a 45%,#6b4a2a)}
.ph-audio{background:linear-gradient(#ffffff,#e6e6e6 70%,#d0d0d0)}
.ph-kitchen{background:linear-gradient(135deg,#9fb7c6,#5b7c90 60%,#c7ced3)}
.product .desc{margin:12px auto 0;width:262px;text-align:center;font-family:"Kalam",cursive;font-weight:700;font-size:18px;text-transform:uppercase;border-bottom:3px solid #c9cacb;line-height:1.3;white-space:nowrap}
.product .buy{display:flex;align-items:center;justify-content:center;gap:6px;margin-top:8px;height:44px;white-space:nowrap}
.product .off{font-family:"Kalam",cursive;font-weight:700;font-size:27px;line-height:1;color:var(--sale-red)}
.cart{display:flex;height:38px;border-radius:19px;overflow:hidden;border:2px solid #2a2a2a;white-space:nowrap}
.cart span{display:flex;align-items:center;padding:0 9px;font-size:14px;font-weight:700;color:#fff}
.cart .price{background:#2a2a2a;color:#ffd050}
.cart.orange .add{background:linear-gradient(#ff8a2a,#d54c00)}
.cart.green .add{background:linear-gradient(#9ad954,#4e9a18)}
/* footer */
.connect{position:absolute;left:0;top:2495px;width:1200px;height:306px}
.connect h3{position:absolute;left:28px;top:18px;font-family:"Kalam",cursive;font-size:29px;font-weight:700}
.social{position:absolute;display:flex;align-items:center;height:40px;border-radius:6px;background:linear-gradient(#f4f4f4,#c9c9c9);color:#333;font-size:13px;font-weight:600;padding-right:12px;gap:10px;overflow:hidden;white-space:nowrap}
.social .sq{width:40px;height:40px;flex:none}
.social.blue{background:linear-gradient(#5d7fc0,#3b5998);color:#fff}
.social .count{background:#fff;color:#333;padding:2px 6px;border-radius:3px}
.connect .or{position:absolute;left:296px;top:86px;font-family:"Kalam",cursive;font-size:24px}
.stat{position:absolute;text-align:center;color:#bfc1c3}
.stat .shape{background:#9a9c9e;margin:0 auto}
.stat b{display:block;font-size:30px;font-weight:800;color:#d8d8d8;line-height:1.1}
.stat small{display:block;font-size:12px;line-height:1.2;white-space:nowrap}
.footer{position:absolute;left:0;top:2801px;width:1200px;height:46px;background:#2a2b2d;display:flex;align-items:center;justify-content:center;font-size:21px;letter-spacing:1px;color:#ddd;text-transform:uppercase;white-space:nowrap}
</style>
</head>
<body>

<header>
  <nav class="topbar">
    <a href="#">What is Voph?</a><a href="#">How to Sell?</a><a href="#">How to Buy?</a>
    <span class="spacer"></span>
    <span class="account"><a href="#">Login</a><a href="#">Register</a></span>
  </nav>
  <span class="tab-flag" style="left:0"></span>

  <div class="header">
    <div class="logo">Voph</div>
    <div class="search">
      <div class="cat">All Categories <span>▼</span></div>
      <div class="field">Item Name</div>
      <div class="go">
        <svg width="22" height="22" viewBox="0 0 22 22"><circle cx="9" cy="9" r="6.5" fill="none" stroke="#3a2a00" stroke-width="3"/><path d="M14 14l6 6" stroke="#3a2a00" stroke-width="3"/></svg>Search</div>
    </div>
    <div class="checkout">
      <svg width="46" height="36" viewBox="0 0 46 36"><path d="M2 4h8l5 20h24l5-14H12" fill="none" stroke="var(--orange)" stroke-width="3"/><circle cx="18" cy="31" r="3" fill="var(--orange)"/><circle cx="36" cy="31" r="3" fill="var(--orange)"/></svg>
      CHECKOUT<span class="arr">▶</span>
    </div>
  </div>

  <nav class="nav">
    <span class="rail"></span>
    <ul>
      <li style="width:98px;position:relative"><svg width="40" height="36" viewBox="0 0 40 36" style="left:29px"><path d="M4 18L20 4l16 14v16H4z" fill="var(--green)"/></svg>Home</li>
      <li style="width:170px;position:relative"><svg width="50" height="36" viewBox="0 0 50 36" style="left:60px"><rect x="4" y="6" width="42" height="26" rx="3" fill="#cfe8b5" stroke="var(--green)" stroke-width="3"/></svg>Electronics</li>
      <li style="width:160px;position:relative"><svg width="36" height="36" viewBox="0 0 36 36" style="left:62px"><circle cx="18" cy="18" r="13" fill="var(--green)"/></svg>Entertainment<br>&amp; Leisure</li>
      <li style="width:115px;position:relative"><svg width="36" height="36" viewBox="0 0 36 36" style="left:40px"><circle cx="18" cy="18" r="13" fill="none" stroke="var(--green)" stroke-width="5"/></svg>Fashion</li>
      <li style="width:130px;position:relative"><svg width="20" height="40" viewBox="0 0 20 40" style="left:55px"><rect x="4" y="6" width="12" height="30" rx="3" fill="#d9ef8a" stroke="var(--green)" stroke-width="2"/></svg>Health<br>&amp; Beauty</li>
      <li style="width:167px;position:relative"><svg width="40" height="36" viewBox="0 0 40 36" style="left:63px"><path d="M6 30C6 14 20 6 34 6c0 14-10 24-28 24z" fill="var(--green)"/></svg>Home &amp; Garden</li>
      <li style="width:130px;position:relative">Jewellery<br>&amp; Watches</li>
      <li style="width:230px;position:relative;border-right:none;padding-left:80px"><svg width="40" height="36" viewBox="0 0 40 36" style="left:150px"><path d="M12 4v30M12 4l18 7-18 7" fill="var(--green)" stroke="var(--green)" stroke-width="3"/></svg>Sports<br>&amp; Outdoors</li>
    </ul>
    <span class="knob"></span>
  </nav>
</header>

<main>
  <section class="carousel" role="img" aria-label="Carousel slide photo: woman with shopping bags on a city street">
    <span class="label" style="left:0;top:40px;width:196px;font-size:15px">A placeholder image, only used for the sake of understanding</span>
    <span class="label" style="left:515px;top:17px">Carousel Slideshow</span>
    <span class="arrow" style="left:0">◀</span>
    <span class="arrow" style="right:0">▶</span>
    <div class="welcome">Welcome to Voph!<br>Change the way you shop!</div>
    <div class="tour">Take a guided tour &gt;&gt;</div>
  </section>

  <aside class="quick">
    <p class="intro hand">Check them out!</p>
    <a href="#">Latest Bargains</a>
    <a href="#">Recently Viewed Bargains</a>
    <a href="#">Ending Soon Bargains</a>
    <a href="#">Popular Bargains</a>
  </aside>

  <form class="newsletter">
    <span class="ask hand">Make sure you never miss a Bargain!</span>
    <span class="email">Enter your email address</span>
    <span class="btn">Subscribe</span>
    <span class="btn rss">Subscribe via RSS <span class="rss-ico"></span></span>
  </form>

  <section class="bargains" style="top:844px">
    <div class="head">Latest Bargains &gt;&gt;<span class="ribbon" style="right:12px;background:var(--green)"></span></div>
    <div class="body">
      <article class="product" style="left:76px"><div class="photo ph-room" role="img" aria-label="Product photo: restaurant interior"></div><p class="desc">Product Description</p><div class="buy"><span class="off">20% off!</span><span class="cart orange"><span class="add">ADD TO CART</span><span class="price">$9.99</span></span></div></article>
      <article class="product" style="left:436px"><div class="photo ph-audio" role="img" aria-label="Product photo: home theatre speakers"></div><p class="desc">Product Description</p><div class="buy"><span class="off">40% off!</span><span class="cart orange"><span class="add">ADD TO CART</span><span class="price">$9.99</span></span></div></article>
      <article class="product" style="left:788px"><div class="photo ph-kitchen" role="img" aria-label="Product photo: kitchen appliances"></div><p class="desc">Product Description</p><div class="buy"><span class="off">20% off!</span><span class="cart orange"><span class="add">ADD TO CART</span><span class="price">$9.99</span></span></div></article>
    </div>
  </section>

  <section class="bargains right" style="top:1259px">
    <div class="head"><span class="ribbon" style="left:12px;background:var(--orange)"></span>&lt;&lt; Recently Viewed Bargains</div>
    <div class="body">
      <article class="product" style="left:76px"><div class="photo ph-room" role="img" aria-label="Product photo: restaurant interior"></div><p class="desc">Product Description</p><div class="buy"><span class="off">20% off!</span><span class="cart green"><span class="add">ADD TO CART</span><span class="price">$9.99</span></span></div></article>
      <article class="product" style="left:436px"><div class="photo ph-audio" role="img" aria-label="Product photo: home theatre speakers"></div><p class="desc">Product Description</p><div class="buy"><span class="off">40% off!</span><span class="cart green"><span class="add">ADD TO CART</span><span class="price">$9.99</span></span></div></article>
      <article class="product" style="left:788px"><div class="photo ph-kitchen" role="img" aria-label="Product photo: kitchen appliances"></div><p class="desc">Product Description</p><div class="buy"><span class="off">20% off!</span><span class="cart green"><span class="add">ADD TO CART</span><span class="price">$9.99</span></span></div></article>
    </div>
  </section>

  <section class="bargains" style="top:1677px">
    <div class="head">Ending Soon Bargains &gt;&gt;<span class="ribbon" style="right:12px;background:var(--green)"></span></div>
    <div class="body">
      <article class="product" style="left:76px"><div class="photo ph-room" role="img" aria-label="Product photo: restaurant interior"></div><p class="desc">Product Description</p><div class="buy"><span class="off">20% off!</span><span class="cart orange"><span class="add">ADD TO CART</span><span class="price">$9.99</span></span></div></article>
      <article class="product" style="left:436px"><div class="photo ph-audio" role="img" aria-label="Product photo: home theatre speakers"></div><p class="desc">Product Description</p><div class="buy"><span class="off">40% off!</span><span class="cart orange"><span class="add">ADD TO CART</span><span class="price">$9.99</span></span></div></article>
      <article class="product" style="left:788px"><div class="photo ph-kitchen" role="img" aria-label="Product photo: kitchen appliances"></div><p class="desc">Product Description</p><div class="buy"><span class="off">20% off!</span><span class="cart orange"><span class="add">ADD TO CART</span><span class="price">$9.99</span></span></div></article>
    </div>
  </section>

  <section class="bargains right" style="top:2092px">
    <div class="head"><span class="ribbon" style="left:12px;background:var(--orange)"></span>&lt;&lt; Popular Bargains</div>
    <div class="body">
      <article class="product" style="left:76px"><div class="photo ph-room" role="img" aria-label="Product photo: restaurant interior"></div><p class="desc">Product Description</p><div class="buy"><span class="off">20% off!</span><span class="cart green"><span class="add">ADD TO CART</span><span class="price">$9.99</span></span></div></article>
      <article class="product" style="left:436px"><div class="photo ph-audio" role="img" aria-label="Product photo: home theatre speakers"></div><p class="desc">Product Description</p><div class="buy"><span class="off">40% off!</span><span class="cart green"><span class="add">ADD TO CART</span><span class="price">$9.99</span></span></div></article>
      <article class="product" style="left:788px"><div class="photo ph-kitchen" role="img" aria-label="Product photo: kitchen appliances"></div><p class="desc">Product Description</p><div class="buy"><span class="off">20% off!</span><span class="cart green"><span class="add">ADD TO CART</span><span class="price">$9.99</span></span></div></article>
    </div>
  </section>
</main>

<footer>
  <section class="connect">
    <h3>let's Connect!</h3>
    <span class="social blue" style="left:62px;top:82px;width:222px"><span class="sq" style="background:#2d4373"></span>Connect with Linkpond</span>
    <span class="or">or</span>
    <span class="social blue" style="left:340px;top:82px;width:136px"><span class="sq" style="background:#2d4373"></span>Share <span class="count">2K</span></span>
    <span class="social" style="left:62px;top:162px;width:208px"><span class="sq" style="background:#3fb3e6"></span>Follow on Quillo</span>
    <span class="social" style="left:290px;top:162px;width:206px"><span class="sq" style="background:#d8d8d8"></span>Connect on Zembra+</span>
    <span class="social" style="left:62px;top:240px;width:208px"><span class="sq" style="background:#1f7fb5"></span>Connect on Workvine</span>
    <span class="social" style="left:290px;top:240px;width:206px"><span class="sq" style="background:#d35ac7"></span>Add to Favorites</span>

    <div class="stat" style="left:665px;top:45px;width:175px"><div class="shape" role="img" aria-label="Delivery truck icon" style="width:170px;height:100px;border-radius:10px"></div></div>
    <div class="stat" style="left:680px;top:55px;width:120px"><b style="color:#333;font-size:24px">XX Units</b><small style="font-weight:700;color:#333">SOLD per day</small></div>
    <div class="stat" style="left:920px;top:45px;width:110px"><div class="shape" role="img" aria-label="Group of people icon" style="width:100px;height:90px;border-radius:40px 40px 6px 6px"></div></div>
    <div class="stat" style="left:1040px;top:60px;width:120px"><b>XX+</b><small>Merchants featured</small></div>
    <div class="stat" style="left:675px;top:165px;width:80px"><div class="shape" role="img" aria-label="Map of the United Kingdom" style="width:72px;height:118px;border-radius:30% 50% 40% 20%"></div></div>
    <div class="stat" style="left:760px;top:180px;width:110px"><small>Shipping to</small><b>XX+</b><small>towns Pan UK</small></div>
    <div class="stat" style="left:940px;top:175px;width:90px"><div class="shape" role="img" aria-label="Shopping bag icon" style="width:78px;height:100px;border-radius:6px"></div></div>
    <div class="stat" style="left:1040px;top:195px;width:120px"><b>XY+</b><small>Listed Goods</small></div>
  </section>
  <nav class="footer">About Us | Contact Us | Customer Enquiry | FAQs | Policy Information</nav>
</footer>

</body>
</html>
```